Vital Spark Electrical in need of a business card design

We need a new business card designed for our electrical business. We have a logo already which I will attach below.
Would like the business card to be..
-BLACK background preferably, possibly white back ground behind logo if colours clash.
-White & Blue (logo blue) text
Something that makes the logo pop, & a modern look. Possibly minimal clean format.

REQUIRE:
-Logo on front & back

TEXT TO INCLUDE (ON ONE SIDE):

Tom Harlow
Director/Electrician
M: 0417 365 208
E:info@vitalsparkelectrical-example.com.au
W:www.vitalsparkelectrical-example.com.au
R.E.C 57318

Custom/New Homes
Renovations
Commercial Office/Shop Fit-outs
Communications & Security Cameras
Electric Vehicle Chargers
Airconditioning
Updates

Requirements
Nice to have
• Possibly even lighten the grey shades for the words 'Vital' & 'Spark' to be more easily read on a black background.

```html
<!DOCTYPE html>
<html lang="en">
<head>
<meta charset="utf-8">
<title>Vital Spark Electrical – Business Card</title>
<link href="https://fonts.googleapis.com/css2?family=Montserrat:wght@600;700&family=Roboto:wght@300;400&display=swap" rel="stylesheet">
<style>
  :root {
    --stage: #2b2d30;
    --slate: #5b6570;
    --slate-light: #66707b;
    --ink: #46505a;
    --blue: #1c9ad8;
    --paper: #ffffff;
    --muted: #6d7379;
  }
  * { box-sizing: border-box; margin: 0; padding: 0; }
  html, body { width: 1200px; height: 960px; overflow: hidden; }
  body {
    background: var(--stage);
    position: relative;
    font-family: "Roboto", sans-serif;
  }
  .card {
    position: absolute;
    left: 280px;
    width: 640px;
    height: 366px;
    border-radius: 4px;
    overflow: hidden;
    box-shadow: 0 10px 24px rgba(0,0,0,.45);
  }

  /* Back side */
  .card-back { top: 84px; background: var(--slate); }
  .card-back .panel-shade {
    position: absolute; right: 0; top: 0;
    width: 300px; height: 366px;
    background: var(--slate-light);
    border-radius: 0 0 0 180px;
    opacity: .55;
  }
  .brand {
    position: absolute;
    display: flex; align-items: center; gap: 12px;
    font-family: "Montserrat", sans-serif;
    font-weight: 700;
    white-space: nowrap;
  }
  .brand-square { width: 26px; height: 26px; }
  .card-back .brand { left: 48px; top: 42px; font-size: 26px; color: var(--paper); }
  .card-back .brand-square { background: var(--paper); }

  .services {
    position: absolute; left: 70px; top: 112px;
    list-style: none;
    font-family: "Montserrat", sans-serif;
    font-weight: 600;
    font-size: 21px;
    color: var(--paper);
  }
  .services li {
    display: flex; align-items: center; gap: 12px;
    height: 36px;
  }
  .services svg { width: 18px; height: 14px; flex: none; }

  /* Front side */
  .card-front { top: 510px; background: var(--paper); }
  .card-front .side-band { position: absolute; inset: 0; }
  .card-front .brand { left: 40px; top: 52px; font-size: 30px; color: var(--ink); }
  .card-front .brand-square { width: 34px; height: 34px; background: var(--blue); border: 4px solid var(--paper); outline: 2px solid var(--ink); }

  .person { position: absolute; left: 228px; top: 150px; }
  .person-name {
    font-family: "Montserrat", sans-serif;
    font-weight: 700; font-size: 28px; color: var(--blue);
  }
  .person-role, .person-licence {
    font-weight: 300; font-size: 17px; color: var(--muted); line-height: 24px;
  }
  .contacts {
    position: absolute; left: 248px; top: 262px;
    list-style: none;
    font-weight: 300; font-size: 16px; color: var(--muted);
  }
  .contacts li { display: flex; align-items: center; gap: 12px; height: 26px; }
  .contacts svg { width: 16px; height: 16px; flex: none; }
</style>
</head>
<body>

<section class="card card-back" aria-label="Business card back">
  <div class="panel-shade"></div>
  <div class="brand"><span class="brand-square"></span>Vital Spark Electrical</div>
  <ul class="services">
    <li><svg viewBox="0 0 18 14"><path d="M1 7h13M9 2l5 5-5 5" fill="none" stroke="#fff" stroke-width="2.2"/></svg>Custom/New Homes</li>
    <li><svg viewBox="0 0 18 14"><path d="M1 7h13M9 2l5 5-5 5" fill="none" stroke="#fff" stroke-width="2.2"/></svg>Renovations</li>
    <li><svg viewBox="0 0 18 14"><path d="M1 7h13M9 2l5 5-5 5" fill="none" stroke="#fff" stroke-width="2.2"/></svg>Commercial Office/Shop Fit-outs</li>
    <li><svg viewBox="0 0 18 14"><path d="M1 7h13M9 2l5 5-5 5" fill="none" stroke="#fff" stroke-width="2.2"/></svg>Communications &amp; Security Cameras</li>
    <li><svg viewBox="0 0 18 14"><path d="M1 7h13M9 2l5 5-5 5" fill="none" stroke="#fff" stroke-width="2.2"/></svg>Electric Vehicle Chargers</li>
    <li><svg viewBox="0 0 18 14"><path d="M1 7h13M9 2l5 5-5 5" fill="none" stroke="#fff" stroke-width="2.2"/></svg>Airconditioning</li>
  </ul>
</section>

<section class="card card-front" aria-label="Business card front">
  <svg class="side-band" viewBox="0 0 640 366" preserveAspectRatio="none" aria-hidden="true">
    <polygon points="0,0 70,0 190,366 0,366" fill="var(--slate)"/>
  </svg>
  <div class="brand"><span class="brand-square"></span>Vital Spark Electrical</div>
  <div class="person">
    <p class="person-name">Tom Harlow</p>
    <p class="person-role">Director/Electrician</p>
    <p class="person-licence">R.E.C 57318</p>
  </div>
  <ul class="contacts">
    <li><svg viewBox="0 0 16 16"><path d="M3 2l3 3-1.5 2a8 8 0 004.5 4.5L11 10l3 3-2 2C6 14 2 10 1 4z" fill="var(--blue)"/></svg>0417 365 208</li>
    <li><svg viewBox="0 0 16 16"><rect x="1" y="3" width="14" height="10" fill="var(--blue)"/><path d="M1 3l7 6 7-6" fill="none" stroke="#fff" stroke-width="1.4"/></svg>info@vitalsparkelectrical-example.com.au</li>
    <li><svg viewBox="0 0 16 16"><circle cx="8" cy="8" r="7" fill="var(--blue)"/><path d="M1 8h14M8 1c3 3 3 11 0 14M8 1c-3 3-3 11 0 14" fill="none" stroke="#fff" stroke-width="1"/></svg>www.vitalsparkelectrical-example.com.au</li>
  </ul>
</section>

</body>
</html>
```